One-page magazine ad for accountant serving the non-profit industry

I am Certified Public Accountant placing a one-page ad in Lanternway Journal. The ad will be seen by churches and other non-profit organizations.
Lanternway Journal requires the following:
Accepted file formats:
a) Press ready PDF with all fonts embedded. OR
b) Flattened CMYK Abode Photoshop PSD or illustrator PDF or EPS with all fonts outlined.
Ad Specs:
Trim 8" x 10.5"
Live 7.5" x 10"
Bleed 8.25" x 10.75"

I would like the ad to state the following information:

Marcus T. Quillby, CPA, CGMA

I am Certified Public Accountant with over 30 years of experience serving the accounting and tax needs of churches and non-profit organizations.

Some of the services I can offer:

Audits, Reviews, Compilations
Bookkeeping Services
Payroll Taxes
501C3 - IRS exemption applications
Clergy Housing Allowance issues and Personal Taxes

```html
<!DOCTYPE html>
<html lang="en">
<head>
<meta charset="utf-8">
<title>Marcus T. Quillby, CPA, CGMA – Advertisement</title>
<link rel="stylesheet" href="https://fonts.googleapis.com/css2?family=Noto+Serif:ital,wght@0,400;0,700;1,700&display=swap">
<style>
  :root {
    --teal: #195c57;
    --teal-dark: #124743;
    --yellow: #fdd835;
    --green: #46e21c;
    --ink: #0e2523;
    --white: #ffffff;
  }
  html, body {
    margin: 0;
    padding: 0;
    overflow: hidden;
    background: #ffffff;
  }
  .ad {
    position: relative;
    width: 887px;
    height: 1200px;
    overflow: hidden;
    background: var(--teal);
    font-family: "Noto Serif", Georgia, serif;
  }
  .hero-photo {
    position: absolute;
    left: 0;
    top: 0;
    width: 608px;
    height: 880px;
  }
  .service-column {
    position: absolute;
    left: 608px;
    top: 0;
    width: 279px;
    height: 1200px;
    background: var(--teal);
  }
  .column-rule {
    position: absolute;
    top: 0;
    width: 3px;
    height: 1200px;
    background: var(--white);
  }
  .column-rule.left { left: 617px; }
  .column-rule.right { left: 863px; }
  .name-plate {
    position: absolute;
    left: 451px;
    top: 49px;
    width: 436px;
    height: 124px;
    background: var(--yellow);
    box-shadow: 0 6px 8px rgba(0, 0, 0, 0.35);
    color: #111;
    text-align: right;
    box-sizing: border-box;
    padding-right: 8px;
  }
  .name-plate .name {
    margin: 10px 0 0;
    font-size: 45px;
    font-weight: 400;
    line-height: 1.15;
    white-space: nowrap;
  }
  .name-plate .credentials {
    margin: 0;
    font-size: 30px;
    line-height: 1.1;
  }
  .profession {
    position: absolute;
    left: 620px;
    width: 243px;
    top: 210px;
    margin: 0;
    text-align: center;
    color: var(--white);
    font-size: 32px;
    font-weight: 400;
    line-height: 42px;
  }
  .services {
    list-style: none;
    margin: 0;
    padding: 0;
  }
  .services li {
    position: absolute;
    left: 620px;
    width: 243px;
    text-align: center;
    color: var(--white);
    font-size: 24px;
    line-height: 34.5px;
  }
  .tagline-band {
    position: absolute;
    left: 0;
    top: 790px;
    width: 608px;
    height: 185px;
  }
  .tagline {
    position: absolute;
    left: 20px;
    top: 828px;
    width: 580px;
    margin: 0;
    text-align: center;
    font-size: 26px;
    font-style: italic;
    font-weight: 700;
    line-height: 42px;
    color: var(--ink);
    transform: rotate(-3.4deg);
    transform-origin: center;
  }
  .contact {
    position: absolute;
    left: 0;
    top: 1024px;
    width: 612px;
    margin: 0;
    text-align: center;
    font-style: normal;
    color: var(--ink);
    font-size: 32px;
    line-height: 43.5px;
  }
</style>
</head>
<body>
<main class="ad">
  <svg class="hero-photo" role="img" aria-label="Photograph of a young green seedling growing from a glass jar filled with coins, on a soft blurred green background" viewBox="0 0 608 880" preserveAspectRatio="none">
    <defs>
      <linearGradient id="photo-bg" x1="0" y1="0" x2="1" y2="1">
        <stop offset="0" stop-color="#5f8f2a"/>
        <stop offset="0.45" stop-color="#9cc23e"/>
        <stop offset="0.75" stop-color="#c9d9a8"/>
        <stop offset="1" stop-color="#e9ece6"/>
      </linearGradient>
      <radialGradient id="photo-jar" cx="0.5" cy="0.6" r="0.5">
        <stop offset="0" stop-color="#8a7a86" stop-opacity="0.7"/>
        <stop offset="1" stop-color="#8a7a86" stop-opacity="0"/>
      </radialGradient>
    </defs>
    <rect width="608" height="880" fill="url(#photo-bg)"/>
    <ellipse cx="330" cy="610" rx="260" ry="220" fill="url(#photo-jar)"/>
  </svg>

  <div class="service-column"></div>
  <div class="column-rule left"></div>
  <div class="column-rule right"></div>

  <header class="name-plate">
    <h1 class="name">Marcus T. Quillby</h1>
    <p class="credentials">CPA, CGMA</p>
  </header>

  <h2 class="profession">Certified<br>Public<br>Accountant</h2>

  <ul class="services">
    <li style="top:453px">Audits</li>
    <li style="top:521px">Reviews</li>
    <li style="top:590px">Compilations</li>
    <li style="top:657px">Bookkeeping<br>Services</li>
    <li style="top:760px">Payroll Taxes</li>
    <li style="top:827px">501C3=IRS<br>Exemption<br>Applications</li>
    <li style="top:964px">Clergy Housing</li>
    <li style="top:1031px">Allowance Issues<br>and Personal<br>Taxes</li>
  </ul>

  <svg class="tagline-band" viewBox="0 0 608 185" preserveAspectRatio="none" aria-hidden="true">
    <path d="M0 50 Q300 28 608 8 L608 162 Q300 168 0 180 Z" fill="rgba(0,0,0,0.25)" transform="translate(0 6)"/>
    <path d="M0 50 Q300 28 608 8 L608 162 Q300 168 0 180 Z" fill="var(--green)"/>
  </svg>
  <p class="tagline">Over 30 years of experience<br>serving the accounting and tax needs of<br>churches and non-profit organizations</p>

  <address class="contact">
    Marcus T. Quillby, CPA, CGMA<br>
    Email: marcus@quillbycpa.com<br>
    (555) 014-2368
  </address>
</main>
</body>
</html>
```